Plate Parade! Digital Order Web App

This is a web app on mobile phone, for consumers to order food inside a restaurant using their phones. we have done up the flow but we need to revamp UI design. pls have a look at our current web on your mobile phone:
https://demo.pesanly.app/o/KWLM/274615

CURRENT DESIGN.
1. food category on left side, always shown. menu items in list view with image.
2. when we click on an item, there is popup page, to select modifiers, or quantity.
3. order review page(cart page) is quite messy now, need a complete new look.
4 payment page(no need to design, handle by Paxtel)
5. order confirmation page. success or error return

DESIGN requirements:
please browse through and click to order with current page above. we have put in lots of thoughts and effort for current flow, the new design should base on this flow.
1. web app. no zoom in/out is allowed for users. responsive html to suit different mobile phone screen size. modern fonts.
2. PAGES needed:
home/welcome page,
well laid out menu items page,
single item page, with add on choice and modifier
cart page(to include recommended items, ordered item list, remove item total, changeable quantity,
confirmation page(success, fail)

DELIVERABLES - responsive html, fonts, images asset such as icons, animation, button images(suitable for commercial use without further third party loyalty fee)

Hi all if we have left a comment on ur design, please revise accordingly and we will conclude it soon!

Target Market(s)

young diners who order food on their mobile phone.

Industry/Entity Type

Restaurant

Coding

Coded - Design and coding required

Number of Pages Required

5+ page

Colors

Designer to choose colors to be used in the design.

Requirements
Must have
• - lively, appetising colors while making the page easy to read. easy on eyes.
• - consistency. fonts used.
Nice to have
• - 2 color schemes
• - html codes. we will top up if you can deliver coded html.
Should not have
• - should not have more than 3 colors
• - should not have more than 3 different fonts
• - should not use colors that are dull

```html
<!DOCTYPE html>
<html lang="en">
<head>
<meta charset="utf-8">
<meta name="viewport" content="width=1200">
<title>Grillo — Menu</title>
<link rel="stylesheet" href="https://fonts.googleapis.com/css2?family=Mulish:wght@400;500;600;700&display=swap">
<style>
:root{
  --brand:#83aaf5;
  --accent:#f5334b;
  --ink:#2f2f33;
  --muted:#8a8a90;
  --sheet:#f8f8f8;
  --card:#ffffff;
  --gap:#ececec;
  --footer:#3b3b3e;
}
*{box-sizing:border-box;margin:0;padding:0}
html,body{width:1200px;height:4092px;overflow:hidden;background:var(--gap)}
body{font-family:"Mulish",sans-serif;color:var(--ink)}
.stage{position:absolute;left:0;top:0;width:755px;height:2576px;transform:scale(1.58940);transform-origin:0 0}
.screen{position:absolute;top:0;width:355px;height:2576px;background:var(--brand);overflow:hidden}
.screen--list{left:0;width:354px}
.screen--nav{left:400px}
.topbar{position:absolute;left:0;right:0;top:0;height:64px}
.brand{position:absolute;left:0;right:0;top:20px;text-align:center;color:#fff;font-size:17px;font-weight:700;letter-spacing:.2px}
.icon-btn{position:absolute;top:22px}
.burger{width:18px;height:16px}
.cart{position:absolute;top:21px;width:22px;height:22px}
.cart-badge{position:absolute;top:-2px;right:-4px;width:10px;height:10px;border-radius:50%;background:var(--accent);color:#fff;font-size:6px;font-weight:700;line-height:10px;text-align:center}
.menu-toggle{position:absolute;top:19px;width:28px;height:28px;border-radius:50%;background:var(--accent);display:flex;align-items:center;justify-content:center}
.sheet{position:absolute;left:0;right:0;top:63px;bottom:0;background:var(--sheet);border-radius:26px 26px 0 0}
.menu{position:absolute;left:26px;right:29px;top:79.5px}
.section-title{height:53.5px;padding-top:12px;line-height:24px;font-size:16.5px;font-weight:600;padding-left:0}
.section-title--first{padding-left:9px}
.item{position:relative;height:82px;margin-bottom:26.5px;background:var(--card);border-radius:4px;box-shadow:0 2px 8px rgba(0,0,0,.06)}
.item-photo{position:absolute;left:9px;top:10px;width:62px;height:62px;border-radius:6px}
.item-name{position:absolute;left:87px;top:9px;font-size:13px;font-weight:500}
.item-alt{position:absolute;left:87px;top:32px;font-size:12px;color:var(--muted)}
.item-price{position:absolute;left:87px;top:55px;font-size:12.5px;color:var(--muted)}
.add-btn{position:absolute;left:253px;top:47px;width:22px;height:22px}
.footer{position:absolute;left:0;right:0;bottom:0;height:21px;background:var(--footer);color:#fff;font-size:5px;display:flex;align-items:center;padding:0 22px}
.footer-links{margin-left:auto;display:flex;gap:12px}
.nav-panel{position:absolute;left:0;right:0;top:0;height:397px;background:var(--brand);border-radius:0 0 24px 24px;box-shadow:0 6px 14px rgba(60,90,160,.25)}
.nav-grid{position:absolute;left:0;right:0;top:76px;display:grid;grid-template-columns:120px 118px 117px;row-gap:28px}
.nav-tile{display:flex;flex-direction:column;align-items:center;color:#fff;font-size:11px;font-weight:500}
.nav-icon{width:44px;height:36px;border:2px solid #fff;border-radius:8px;margin-bottom:7px;display:flex;align-items:center;justify-content:center}
</style>
</head>
<body>
<div class="stage">

  <!-- Menu list screen -->
  <section class="screen screen--list">
    <header class="topbar">
      <svg class="icon-btn burger" style="left:17px" viewBox="0 0 18 16"><g stroke="#fff" stroke-width="2"><line x1="0" y1="2" x2="18" y2="2"/><line x1="0" y1="8" x2="18" y2="8"/><line x1="0" y1="14" x2="18" y2="14"/></g></svg>
      <div class="brand">Grillo</div>
      <div class="cart" style="left:272px">
        <svg viewBox="0 0 22 22" width="22" height="22" fill="none" stroke="#fff" stroke-width="1.8"><path d="M1 3h3l3 11h11l2-8H6"/><circle cx="8.5" cy="18.5" r="1.5"/><circle cx="16.5" cy="18.5" r="1.5"/></svg>
        <span class="cart-badge">2</span>
      </div>
      <svg class="icon-btn burger" style="left:316px;top:26px" viewBox="0 0 18 16"><g stroke="#fff" stroke-width="2"><line x1="0" y1="2" x2="18" y2="2"/><line x1="0" y1="8" x2="18" y2="8"/><line x1="0" y1="14" x2="18" y2="14"/></g></svg>
    </header>
    <div class="sheet"></div>
    <main class="menu">
      <h2 class="section-title section-title--first">Vegetables</h2>
      <article class="item"><div class="item-photo" role="img" aria-label="Grilled romaine lettuce" style="background:linear-gradient(135deg,#7ea24a,#c9d98a)"></div><h3 class="item-name">Grilled Romaine Lettuce</h3><p class="item-alt">烤油麦菜</p><p class="item-price">Price : $ 1.30</p><svg class="add-btn" viewBox="0 0 22 22"><circle cx="11" cy="11" r="11" fill="#f5334b"/><path d="M11 5v12M5 11h12" stroke="#fff" stroke-width="2.4"/></svg></article>
      <article class="item"><div class="item-photo" role="img" aria-label="Grilled oyster mushroom skewers" style="background:linear-gradient(135deg,#6b3f1e,#c58a4a)"></div><h3 class="item-name">Grilled Oyster Mushroom</h3><p class="item-alt">烤耗菇</p><p class="item-price">Price : $1.30</p><svg class="add-btn" viewBox="0 0 22 22"><circle cx="11" cy="11" r="11" fill="#f5334b"/><path d="M11 5v12M5 11h12" stroke="#fff" stroke-width="2.4"/></svg></article>
      <article class="item"><div class="item-photo" role="img" aria-label="Grilled king oyster mushroom" style="background:linear-gradient(135deg,#c9780e,#f2c14e)"></div><h3 class="item-name">Grilled Pleurotus Eryngii</h3><p class="item-alt">烤杏□菇</p><p class="item-price">Price : $ 1.50</p><svg class="add-btn" viewBox="0 0 22 22"><circle cx="11" cy="11" r="11" fill="#f5334b"/><path d="M11 5v12M5 11h12" stroke="#fff" stroke-width="2.4"/></svg></article>
      <article class="item"><div class="item-photo" role="img" aria-label="Grilled string beans" style="background:linear-gradient(135deg,#3d6b2a,#8cbf5a)"></div><h3 class="item-name">Grilled String Bean</h3><p class="item-alt">烤四季豆</p><p class="item-price">Price : $ 1.30</p><svg class="add-btn" viewBox="0 0 22 22"><circle cx="11" cy="11" r="11" fill="#f5334b"/><path d="M11 5v12M5 11h12" stroke="#fff" stroke-width="2.4"/></svg></article>

      <h2 class="section-title">Meat</h2>
      <article class="item"><div class="item-photo" role="img" aria-label="Grilled mutton skewers" style="background:linear-gradient(135deg,#6e1f16,#c25a3f)"></div><h3 class="item-name">Grilled Mutton BBQ</h3><p class="item-alt">烤羊肉串</p><p class="item-price">Price : $ 1.00</p><svg class="add-btn" viewBox="0 0 22 22"><circle cx="11" cy="11" r="11" fill="#f5334b"/><path d="M11 5v12M5 11h12" stroke="#fff" stroke-width="2.4"/></svg></article>
      <article class="item"><div class="item-photo" role="img" aria-label="Lamb skewers over charcoal" style="background:linear-gradient(135deg,#8a3b0e,#e79a2e)"></div><h3 class="item-name">Lamb W/ Red Switch</h3><p class="item-alt">□柳枝羔羊</p><p class="item-price">Price : $ 2.80</p><svg class="add-btn" viewBox="0 0 22 22"><circle cx="11" cy="11" r="11" fill="#f5334b"/><path d="M11 5v12M5 11h12" stroke="#fff" stroke-width="2.4"/></svg></article>
      <article class="item"><div class="item-photo" role="img" aria-label="Grilled beef skewers" style="background:linear-gradient(135deg,#5a2a18,#a7663f)"></div><h3 class="item-name">Grilled Beef Finger</h3><p class="item-alt">烤牛肉</p><p class="item-price">Price : $ 1.00</p><svg class="add-btn" viewBox="0 0 22 22"><circle cx="11" cy="11" r="11" fill="#f5334b"/><path d="M11 5v12M5 11h12" stroke="#fff" stroke-width="2.4"/></svg></article>
      <article class="item"><div class="item-photo" role="img" aria-label="Grilled chicken skewers" style="background:linear-gradient(135deg,#c98a12,#f3d064)"></div><h3 class="item-name">Girlled Chicken Meat</h3><p class="item-alt">烤□肉</p><p class="item-price">Price : $ 1.00</p><svg class="add-btn" viewBox="0 0 22 22"><circle cx="11" cy="11" r="11" fill="#f5334b"/><path d="M11 5v12M5 11h12" stroke="#fff" stroke-width="2.4"/></svg></article>

      <h2 class="section-title">Seafood</h2>
      <article class="item"><div class="item-photo" role="img" aria-label="Grilled abalone in shells" style="background:linear-gradient(135deg,#8a6a4a,#e6c9a0)"></div><h3 class="item-name">Grilled Abalone (3 Pcs)</h3><p class="item-alt">碳烤□□(3粒)</p><p class="item-price">Price : $ 19.80</p><svg class="add-btn" viewBox="0 0 22 22"><circle cx="11" cy="11" r="11" fill="#f5334b"/><path d="M11 5v12M5 11h12" stroke="#fff" stroke-width="2.4"/></svg></article>
      <article class="item"><div class="item-photo" role="img" aria-label="Grilled oysters" style="background:linear-gradient(135deg,#9a7a50,#efd8a8)"></div><h3 class="item-name">Grilled Oyster(3Pcs)</h3><p class="item-alt">碳烤生蚝(3粒)</p><p class="item-price">Price : $ 18.80</p><svg class="add-btn" viewBox="0 0 22 22"><circle cx="11" cy="11" r="11" fill="#f5334b"/><path d="M11 5v12M5 11h12" stroke="#fff" stroke-width="2.4"/></svg></article>
      <article class="item"><div class="item-photo" role="img" aria-label="Grilled squid tentacles" style="background:linear-gradient(135deg,#4a2410,#b0602c)"></div><h3 class="item-name">Grilled Tentacles Of Squid</h3><p class="item-alt">碳烤□□□</p><p class="item-price">Price : $ 5.80</p><svg class="add-btn" viewBox="0 0 22 22"><circle cx="11" cy="11" r="11" fill="#f5334b"/><path d="M11 5v12M5 11h12" stroke="#fff" stroke-width="2.4"/></svg></article>
      <article class="item"><div class="item-photo" role="img" aria-label="Grilled prawn skewers" style="background:linear-gradient(135deg,#3a2a22,#d0603a)"></div><h3 class="item-name">Grilled Fresh Prawn</h3><p class="item-alt">碳烤海□□□串</p><p class="item-price">Price : $ 1.00</p><svg class="add-btn" viewBox="0 0 22 22"><circle cx="11" cy="11" r="11" fill="#f5334b"/><path d="M11 5v12M5 11h12" stroke="#fff" stroke-width="2.4"/></svg></article>

      <h2 class="section-title">Special</h2>
      <article class="item"><div class="item-photo" role="img" aria-label="Grilled sweet potato pieces" style="background:linear-gradient(135deg,#c9600e,#f4a640)"></div><h3 class="item-name">Grilled Sweet Potato Pieces</h3><p class="item-alt">吊炉地瓜□</p><p class="item-price">Price : $ 2.20</p><svg class="add-btn" viewBox="0 0 22 22"><circle cx="11" cy="11" r="11" fill="#f5334b"/><path d="M11 5v12M5 11h12" stroke="#fff" stroke-width="2.4"/></svg></article>
      <article class="item"><div class="item-photo" role="img" aria-label="Grilled pineapple skewers" style="background:linear-gradient(135deg,#5a3a14,#e0a428)"></div><h3 class="item-name">Grilled Pineapple</h3><p class="item-alt">吊炉黄梨串</p><p class="item-price">Price : $ 3.20</p><svg class="add-btn" viewBox="0 0 22 22"><circle cx="11" cy="11" r="11" fill="#f5334b"/><path d="M11 5v12M5 11h12" stroke="#fff" stroke-width="2.4"/></svg></article>
      <article class="item"><div class="item-photo" role="img" aria-label="Garlic chicken wings" style="background:linear-gradient(135deg,#9a4a18,#eaa060)"></div><h3 class="item-name">Garlic Chicken Winglet(3Pcs)</h3><p class="item-alt">蒜香□中翅(3粒)</p><p class="item-price">Price : $ 3.50</p><svg class="add-btn" viewBox="0 0 22 22"><circle cx="11" cy="11" r="11" fill="#f5334b"/><path d="M11 5v12M5 11h12" stroke="#fff" stroke-width="2.4"/></svg></article>
      <article class="item"><div class="item-photo" role="img" aria-label="Grilled pig trotter" style="background:linear-gradient(135deg,#6a2c1a,#c87a50)"></div><h3 class="item-name">Grilled Pig Trotter</h3><p class="item-alt">吊炉猪手</p><p class="item-price">Price : $ 3.00</p><svg class="add-btn" viewBox="0 0 22 22"><circle cx="11" cy="11" r="11" fill="#f5334b"/><path d="M11 5v12M5 11h12" stroke="#fff" stroke-width="2.4"/></svg></article>

      <h2 class="section-title">Cold Dish</h2>
      <article class="item"><div class="item-photo" role="img" aria-label="Seafood enoki mushroom salad" style="background:linear-gradient(135deg,#5a8a3a,#e8b070)"></div><h3 class="item-name">Seafood Enoki Mushroom</h3><p class="item-alt">□□海□金□菇</p><p class="item-price">Price : $ 12.80</p><svg class="add-btn" viewBox="0 0 22 22"><circle cx="11" cy="11" r="11" fill="#f5334b"/><path d="M11 5v12M5 11h12" stroke="#fff" stroke-width="2.4"/></svg></article>
      <article class="item"><div class="item-photo" role="img" aria-label="Sukiyaki platter" style="background:linear-gradient(135deg,#b04a3a,#f0d8c0)"></div><h3 class="item-name">Sukiyaki</h3><p class="item-alt">日式寿喜□</p><p class="item-price">Price : $ 15.80</p><svg class="add-btn" viewBox="0 0 22 22"><circle cx="11" cy="11" r="11" fill="#f5334b"/><path d="M11 5v12M5 11h12" stroke="#fff" stroke-width="2.4"/></svg></article>
      <article class="item"><div class="item-photo" role="img" aria-label="Tinfoil brain flower dish" style="background:linear-gradient(135deg,#7a2a18,#d8703a)"></div><h3 class="item-name">Tinfoil Brain Flower</h3><p class="item-alt">□□□花</p><p class="item-price">Price : $ 9.80</p><svg class="add-btn" viewBox="0 0 22 22"><circle cx="11" cy="11" r="11" fill="#f5334b"/><path d="M11 5v12M5 11h12" stroke="#fff" stroke-width="2.4"/></svg></article>
      <article class="item"><div class="item-photo" role="img" aria-label="Dongbei cold noodle salad" style="background:linear-gradient(135deg,#8aa04a,#f0e0b0)"></div><h3 class="item-name">Dongbei Cold Dish</h3><p class="item-alt">□北凉拌菜</p><p class="item-price">Price : $ 7.80</p><svg class="add-btn" viewBox="0 0 22 22"><circle cx="11" cy="11" r="11" fill="#f5334b"/><path d="M11 5v12M5 11h12" stroke="#fff" stroke-width="2.4"/></svg></article>
    </main>
    <footer class="footer"><span>copyright2019grillo</span><span class="footer-links"><span>Terms &amp; Conditions</span><span>Privacy Policy</span></span></footer>
  </section>

  <!-- Category navigation open -->
  <section class="screen screen--nav">
    <div class="sheet"></div>
    <main class="menu">
      <h2 class="section-title section-title--first">Vegetables</h2>
      <article class="item"><div class="item-photo" role="img" aria-label="Grilled romaine lettuce" style="background:linear-gradient(135deg,#7ea24a,#c9d98a)"></div><h3 class="item-name">Grilled Romaine Lettuce</h3><p class="item-alt">烤油麦菜</p><p class="item-price">Price : $ 1.30</p></article>
      <article class="item"><div class="item-photo" role="img" aria-label="Grilled oyster mushroom skewers" style="background:linear-gradient(135deg,#6b3f1e,#c58a4a)"></div><h3 class="item-name">Grilled Oyster Mushroom</h3><p class="item-alt">烤耗菇</p><p class="item-price">Price : $1.30</p></article>
      <article class="item"><div class="item-photo" role="img" aria-label="Grilled king oyster mushroom" style="background:linear-gradient(135deg,#c9780e,#f2c14e)"></div><h3 class="item-name">Grilled Pleurotus Eryngii</h3><p class="item-alt">烤杏□菇</p><p class="item-price">Price : $ 1.50</p><svg class="add-btn" viewBox="0 0 22 22"><circle cx="11" cy="11" r="11" fill="#f5334b"/><path d="M11 5v12M5 11h12" stroke="#fff" stroke-width="2.4"/></svg></article>
      <article class="item"><div class="item-photo" role="img" aria-label="Grilled string beans" style="background:linear-gradient(135deg,#3d6b2a,#8cbf5a)"></div><h3 class="item-name">Grilled String Bean</h3><p class="item-alt">烤四季豆</p><p class="item-price">Price : $ 1.30</p><svg class="add-btn" viewBox="0 0 22 22"><circle cx="11" cy="11" r="11" fill="#f5334b"/><path d="M11 5v12M5 11h12" stroke="#fff" stroke-width="2.4"/></svg></article>

      <h2 class="section-title">Meat</h2>
      <article class="item"><div class="item-photo" role="img" aria-label="Grilled mutton skewers" style="background:linear-gradient(135deg,#6e1f16,#c25a3f)"></div><h3 class="item-name">Grilled Mutton BBQ</h3><p class="item-alt">烤羊肉串</p><p class="item-price">Price : $ 1.00</p><svg class="add-btn" viewBox="0 0 22 22"><circle cx="11" cy="11" r="11" fill="#f5334b"/><path d="M11 5v12M5 11h12" stroke="#fff" stroke-width="2.4"/></svg></article>
      <article class="item"><div class="item-photo" role="img" aria-label="Lamb skewers over charcoal" style="background:linear-gradient(135deg,#8a3b0e,#e79a2e)"></div><h3 class="item-name">Lamb W/ Red Switch</h3><p class="item-alt">□柳枝羔羊</p><p class="item-price">Price : $ 2.80</p><svg class="add-btn" viewBox="0 0 22 22"><circle cx="11" cy="11" r="11" fill="#f5334b"/><path d="M11 5v12M5 11h12" stroke="#fff" stroke-width="2.4"/></svg></article>
      <article class="item"><div class="item-photo" role="img" aria-label="Grilled beef skewers" style="background:linear-gradient(135deg,#5a2a18,#a7663f)"></div><h3 class="item-name">Grilled Beef Finger</h3><p class="item-alt">烤牛肉</p><p class="item-price">Price : $ 1.00</p><svg class="add-btn" viewBox="0 0 22 22"><circle cx="11" cy="11" r="11" fill="#f5334b"/><path d="M11 5v12M5 11h12" stroke="#fff" stroke-width="2.4"/></svg></article>
      <article class="item"><div class="item-photo" role="img" aria-label="Grilled chicken skewers" style="background:linear-gradient(135deg,#c98a12,#f3d064)"></div><h3 class="item-name">Girlled Chicken Meat</h3><p class="item-alt">烤□肉</p><p class="item-price">Price : $ 1.00</p><svg class="add-btn" viewBox="0 0 22 22"><circle cx="11" cy="11" r="11" fill="#f5334b"/><path d="M11 5v12M5 11h12" stroke="#fff" stroke-width="2.4"/></svg></article>

      <h2 class="section-title">Seafood</h2>
      <article class="item"><div class="item-photo" role="img" aria-label="Grilled abalone in shells" style="background:linear-gradient(135deg,#8a6a4a,#e6c9a0)"></div><h3 class="item-name">Grilled Abalone (3 Pcs)</h3><p class="item-alt">碳烤□□(3粒)</p><p class="item-price">Price : $ 19.80</p><svg class="add-btn" viewBox="0 0 22 22"><circle cx="11" cy="11" r="11" fill="#f5334b"/><path d="M11 5v12M5 11h12" stroke="#fff" stroke-width="2.4"/></svg></article>
      <article class="item"><div class="item-photo" role="img" aria-label="Grilled oysters" style="background:linear-gradient(135deg,#9a7a50,#efd8a8)"></div><h3 class="item-name">Grilled Oyster(3Pcs)</h3><p class="item-alt">碳烤生蚝(3粒)</p><p class="item-price">Price : $ 18.80</p><svg class="add-btn" viewBox="0 0 22 22"><circle cx="11" cy="11" r="11" fill="#f5334b"/><path d="M11 5v12M5 11h12" stroke="#fff" stroke-width="2.4"/></svg></article>
      <article class="item"><div class="item-photo" role="img" aria-label="Grilled squid tentacles" style="background:linear-gradient(135deg,#4a2410,#b0602c)"></div><h3 class="item-name">Grilled Tentacles Of Squid</h3><p class="item-alt">碳烤□□□</p><p class="item-price">Price : $ 5.80</p><svg class="add-btn" viewBox="0 0 22 22"><circle cx="11" cy="11" r="11" fill="#f5334b"/><path d="M11 5v12M5 11h12" stroke="#fff" stroke-width="2.4"/></svg></article>
      <article class="item"><div class="item-photo" role="img" aria-label="Grilled prawn skewers" style="background:linear-gradient(135deg,#3a2a22,#d0603a)"></div><h3 class="item-name">Grilled Fresh Prawn</h3><p class="item-alt">碳烤海□□□串</p><p class="item-price">Price : $ 1.00</p><svg class="add-btn" viewBox="0 0 22 22"><circle cx="11" cy="11" r="11" fill="#f5334b"/><path d="M11 5v12M5 11h12" stroke="#fff" stroke-width="2.4"/></svg></article>

      <h2 class="section-title">Special</h2>
      <article class="item"><div class="item-photo" role="img" aria-label="Grilled sweet potato pieces" style="background:linear-gradient(135deg,#c9600e,#f4a640)"></div><h3 class="item-name">Grilled Sweet Potato Pieces</h3><p class="item-alt">吊炉地瓜□</p><p class="item-price">Price : $ 2.20</p><svg class="add-btn" viewBox="0 0 22 22"><circle cx="11" cy="11" r="11" fill="#f5334b"/><path d="M11 5v12M5 11h12" stroke="#fff" stroke-width="2.4"/></svg></article>
      <article class="item"><div class="item-photo" role="img" aria-label="Grilled pineapple skewers" style="background:linear-gradient(135deg,#5a3a14,#e0a428)"></div><h3 class="item-name">Grilled Pineapple</h3><p class="item-alt">吊炉黄梨串</p><p class="item-price">Price : $ 3.20</p><svg class="add-btn" viewBox="0 0 22 22"><circle cx="11" cy="11" r="11" fill="#f5334b"/><path d="M11 5v12M5 11h12" stroke="#fff" stroke-width="2.4"/></svg></article>
      <article class="item"><div class="item-photo" role="img" aria-label="Garlic chicken wings" style="background:linear-gradient(135deg,#9a4a18,#eaa060)"></div><h3 class="item-name">Garlic Chicken Winglet(3Pcs)</h3><p class="item-alt">蒜香□中翅(3粒)</p><p class="item-price">Price : $ 3.50</p><svg class="add-btn" viewBox="0 0 22 22"><circle cx="11" cy="11" r="11" fill="#f5334b"/><path d="M11 5v12M5 11h12" stroke="#fff" stroke-width="2.4"/></svg></article>
      <article class="item"><div class="item-photo" role="img" aria-label="Grilled pig trotter" style="background:linear-gradient(135deg,#6a2c1a,#c87a50)"></div><h3 class="item-name">Grilled Pig Trotter</h3><p class="item-alt">吊炉猪手</p><p class="item-price">Price : $ 3.00</p><svg class="add-btn" viewBox="0 0 22 22"><circle cx="11" cy="11" r="11" fill="#f5334b"/><path d="M11 5v12M5 11h12" stroke="#fff" stroke-width="2.4"/></svg></article>

      <h2 class="section-title">Cold Dish</h2>
      <article class="item"><div class="item-photo" role="img" aria-label="Seafood enoki mushroom salad" style="background:linear-gradient(135deg,#5a8a3a,#e8b070)"></div><h3 class="item-name">Seafood Enoki Mushroom</h3><p class="item-alt">□□海□金□菇</p><p class="item-price">Price : $ 12.80</p><svg class="add-btn" viewBox="0 0 22 22"><circle cx="11" cy="11" r="11" fill="#f5334b"/><path d="M11 5v12M5 11h12" stroke="#fff" stroke-width="2.4"/></svg></article>
      <article class="item"><div class="item-photo" role="img" aria-label="Sukiyaki platter" style="background:linear-gradient(135deg,#b04a3a,#f0d8c0)"></div><h3 class="item-name">Sukiyaki</h3><p class="item-alt">日式寿喜□</p><p class="item-price">Price : $ 15.80</p><svg class="add-btn" viewBox="0 0 22 22"><circle cx="11" cy="11" r="11" fill="#f5334b"/><path d="M11 5v12M5 11h12" stroke="#fff" stroke-width="2.4"/></svg></article>
      <article class="item"><div class="item-photo" role="img" aria-label="Tinfoil brain flower dish" style="background:linear-gradient(135deg,#7a2a18,#d8703a)"></div><h3 class="item-name">Tinfoil Brain Flower</h3><p class="item-alt">□□□花</p><p class="item-price">Price : $ 9.80</p><svg class="add-btn" viewBox="0 0 22 22"><circle cx="11" cy="11" r="11" fill="#f5334b"/><path d="M11 5v12M5 11h12" stroke="#fff" stroke-width="2.4"/></svg></article>
      <article class="item"><div class="item-photo" role="img" aria-label="Dongbei cold noodle salad" style="background:linear-gradient(135deg,#8aa04a,#f0e0b0)"></div><h3 class="item-name">Dongbei Cold Dish</h3><p class="item-alt">□北凉拌菜</p><p class="item-price">Price : $ 7.80</p><svg class="add-btn" viewBox="0 0 22 22"><circle cx="11" cy="11" r="11" fill="#f5334b"/><path d="M11 5v12M5 11h12" stroke="#fff" stroke-width="2.4"/></svg></article>
    </main>
    <footer class="footer"><span>copyright2019grillo</span><span class="footer-links"><span>Terms &amp; Conditions</span><span>Privacy Policy</span></span></footer>

    <nav class="nav-panel">
      <header class="topbar">
        <svg class="icon-btn burger" style="left:17px" viewBox="0 0 18 16"><g stroke="#fff" stroke-width="2"><line x1="0" y1="2" x2="18" y2="2"/><line x1="0" y1="8" x2="18" y2="8"/><line x1="0" y1="14" x2="18" y2="14"/></g></svg>
        <div class="brand">Grillo</div>
        <div class="cart" style="left:272px">
          <svg viewBox="0 0 22 22" width="22" height="22" fill="none" stroke="#fff" stroke-width="1.8"><path d="M1 3h3l3 11h11l2-8H6"/><circle cx="8.5" cy="18.5" r="1.5"/><circle cx="16.5" cy="18.5" r="1.5"/></svg>
          <span class="cart-badge">2</span>
        </div>
        <div class="menu-toggle" style="left:311px">
          <svg width="16" height="14" viewBox="0 0 16 14"><g stroke="#fff" stroke-width="2"><line x1="0" y1="2" x2="16" y2="2"/><line x1="0" y1="7" x2="16" y2="7"/><line x1="0" y1="12" x2="16" y2="12"/></g></svg>
        </div>
      </header>
      <div class="nav-grid">
        <a class="nav-tile"><span class="nav-icon" role="img" aria-label="Vegetables icon"></span>Vegetables</a>
        <a class="nav-tile"><span class="nav-icon" role="img" aria-label="Meat icon"></span>Meat</a>
        <a class="nav-tile"><span class="nav-icon" role="img" aria-label="Seafood icon"></span>Sea Food</a>
        <a class="nav-tile"><span class="nav-icon" role="img" aria-label="Special dishes icon"></span>Special</a>
        <a class="nav-tile"><span class="nav-icon" role="img" aria-label="Cold dish icon"></span>Cold Dish</a>
        <a class="nav-tile"><span class="nav-icon" role="img" aria-label="Main dishes icon"></span>Main</a>
        <a class="nav-tile"><span class="nav-icon" role="img" aria-label="Set meals icon"></span>Set</a>
        <a class="nav-tile"><span class="nav-icon" role="img" aria-label="Juice icon"></span>Juice</a>
        <a class="nav-tile"><span class="nav-icon" role="img" aria-label="Wine icon"></span>Wine</a>
        <a class="nav-tile"><span class="nav-icon" role="img" aria-label="Beer icon"></span>Beer</a>
        <a class="nav-tile"><span class="nav-icon" role="img" aria-label="Alcohol icon"></span>Alcohol</a>
        <a class="nav-tile"><span class="nav-icon" role="img" aria-label="Drinks icon"></span>Drinks</a>
      </div>
    </nav>
  </section>

</div>
</body>
</html>
```